LA Billboard Project for Brisk Lending

We are running three different billboards around LA, and we need someone to take the mock-ups I've created and bring this campaign to life. Whatever wording is on the mock-ups should stay the same in the ads you create, but feel free to get creative with layout and style. I've attached our mock-ups, our style guide, our logo, and the necessary specs for the billboards. If you have any questions, feel free to reach out!

```html
<!DOCTYPE html>
<html lang="en">
<head>
<meta charset="utf-8">
<title>Brisk Lending — LA Billboards</title>
<link href="https://fonts.googleapis.com/css2?family=Outfit:wght@400;600&display=swap" rel="stylesheet">
<style>
  :root {
    --navy: #0c2340;
    --yellow: #f7dd1c;
    --cyan: #4dbdd6;
    --white: #ffffff;
    --page: #ffffff;
  }
  * { margin: 0; padding: 0; box-sizing: border-box; }
  html, body { width: 1200px; height: 1200px; overflow: hidden; background: var(--page); }
  body { position: relative; font-family: "Outfit", sans-serif; }

  .billboard {
    position: absolute;
    left: 80px;
    width: 1040px;
    height: 478px;
    background: var(--navy);
    overflow: hidden;
  }
  .billboard--traffic { top: 100px; }
  .billboard--strategy { top: 622px; }

  .billboard__photo {
    position: absolute;
    top: 0;
    right: 0;
    width: 460px;
    height: 100%;
  }
  .billboard--traffic .billboard__photo {
    background: linear-gradient(170deg, #b9cbd6 0%, #c9a063 30%, #8d8f8c 58%, #6f7a84 100%);
  }
  .billboard--strategy .billboard__photo {
    background: linear-gradient(180deg, #8fa9c4 0%, #e3b9a8 32%, #b7a58f 58%, #5e6b4c 100%);
  }

  .billboard__rule {
    position: absolute;
    top: 0;
    right: 460px;
    width: 12px;
    height: 100%;
    background: var(--yellow);
  }

  .billboard__headline {
    position: absolute;
    left: 53px;
    color: var(--white);
    font-weight: 600;
    letter-spacing: -0.02em;
  }
  .billboard--traffic .billboard__headline { top: 60px; font-size: 98px; line-height: 0.94; }
  .billboard--strategy .billboard__headline { top: 48px; font-size: 90px; line-height: 0.88; }

  .billboard__tagline {
    position: absolute;
    left: 54px;
    top: 282px;
    color: var(--yellow);
    font-weight: 400;
    font-size: 40px;
    line-height: 1.15;
  }

  .billboard__url {
    position: absolute;
    left: 54px;
    color: var(--white);
    font-weight: 400;
    font-size: 29px;
  }
  .billboard--traffic .billboard__url { top: 418px; }
  .billboard--strategy .billboard__url { top: 412px; }

  .brand-mark {
    position: absolute;
    top: 0;
    left: 870px;
    width: 122px;
    height: 123px;
    background: var(--navy);
    display: flex;
    flex-direction: column;
    align-items: center;
    justify-content: center;
    color: var(--cyan);
    font-weight: 600;
    font-size: 25px;
    line-height: 1.05;
    text-align: center;
  }
</style>
</head>
<body>

<section class="billboard billboard--traffic">
  <div class="billboard__photo" role="img" aria-label="Photo of busy downtown Los Angeles freeway traffic with city towers and palm trees"></div>
  <div class="billboard__rule"></div>
  <h1 class="billboard__headline">traffic<br>is a mess</h1>
  <p class="billboard__tagline">Your mortgage<br>doesn’t have to be</p>
  <p class="billboard__url">briskapply.com</p>
  <div class="brand-mark"><span>Brisk</span><span>Lending</span></div>
</section>

<section class="billboard billboard--strategy">
  <div class="billboard__photo" role="img" aria-label="Photo of the Los Angeles skyline at sunset with palm trees and rooftops"></div>
  <div class="billboard__rule"></div>
  <h1 class="billboard__headline">what’s<br>your<br>mortgage<br>strategy?</h1>
  <p class="billboard__url">briskrefi.com</p>
  <div class="brand-mark"><span>Brisk</span><span>Lending</span></div>
</section>

</body>
</html>
```